IT Tradingsystem for car dealers needs Business Card Design

We need a fresh and modern design for our new business cards.

We develop a it-business system for car dealers in Sweden, Norway and on our way down to further countries in Europe, hence the namechange to BrolaTek Europe AB. The site can be found at www.brolatek-example.com. The startpage is also in for an update/modernization soon so don't take to much from here.

We are looking to print double sided, 4-colour cards.

We want to look professional, modern and serious. Open to cooler suggestions, but not too crazy. We need to make a good and serious impression on our potential customers. It needs to reflect our scandinavian design values and layout.

Preferably with the full BrolaTek logo in good size on the back, so the small print on the logo can be read easily.

Text that needs to go on the cards:
-------

Per Oskar Fjellström
Founder

Direct +46 70-512 96 47
Support 08-612 57 394
po.fjellstrom@brolatek-example.com

BrolaTek Europe AB
Box 8617
104 29 Stockholm

Brolatek-example.com
Saljportalen-example.se

--------
Good luck and thanks!

PS. If you need more input or see what our previous cards looked like, don't hesitate to contact me!

Target Market(s)

Decision makers / executives at brand cardealers

Industry/Entity Type

Automotive

Contact Information for Business Card

Normal size

Requirements
Must have
• Full logo
Nice to have
• Base on our orange colors
Should not have
• No fonts with serif, and not too much graphics

```html
<!DOCTYPE html>
<html lang="sv">
<head>
<meta charset="utf-8">
<title>BrolaTek – visitkort</title>
<link rel="stylesheet" href="https://fonts.googleapis.com/css2?family=Lato:wght@400;700&display=swap">
<style>
  :root {
    --stage: #222222;
    --orange: #f47920;
    --orange-soft: #f89b5e;
    --ink: #231f20;
    --paper: #ffffff;
  }
  * { margin: 0; padding: 0; box-sizing: border-box; }
  html, body { width: 1189px; height: 1200px; overflow: hidden; }
  body {
    background: var(--stage);
    font-family: "Lato", sans-serif;
    position: relative;
  }
  .card {
    position: absolute;
    left: 171px;
    width: 855px;
    height: 488px;
    overflow: hidden;
    box-shadow: 6px 8px 14px rgba(0,0,0,0.55);
  }
  .card--back { top: 67px; background: var(--orange); color: var(--paper); }
  .card--front { top: 626px; background: var(--paper); color: var(--ink); }
  .card > * { position: absolute; white-space: nowrap; z-index: 1; }

  /* Back */
  .brand-mark {
    left: 145px; top: 200px;
    width: 80px; height: 80px;
    background: var(--paper);
  }
  .brand-name {
    font-weight: 700;
    font-size: 78px;
    line-height: 1;
    letter-spacing: -1px;
  }
  .card--back .brand-name { left: 268px; top: 192px; }
  .tagline { font-size: 17.5px; letter-spacing: 0.5px; line-height: 1; word-spacing: 2px; }
  .card--back .tagline { left: 272px; top: 277px; }
  .web-links {
    left: 0; right: 0; top: 389px;
    text-align: center; font-size: 22px; line-height: 1;
  }

  /* Front */
  .card--front .brand-name { left: 49px; top: 52px; color: var(--ink); }
  .card--front .tagline { left: 51px; top: 127px; }
  .person-name { left: 49px; top: 195px; font-weight: 700; font-size: 29px; line-height: 1.2; }
  .person-role { left: 49px; top: 228px; font-size: 22px; color: var(--orange); line-height: 1.2; }
  .address { left: 49px; top: 265px; font-size: 23px; line-height: 29px; }
  .contacts { left: 49px; top: 373px; font-size: 23px; line-height: 28.5px; }
  .contacts .label { color: var(--orange); }
  .card--front .decor-block {
    left: 510px; top: 0;
    width: 345px; height: 488px;
    z-index: 0;
    background: linear-gradient(160deg, var(--orange) 0%, var(--orange) 55%, var(--orange-soft) 100%);
  }
</style>
</head>
<body>
  <section class="card card--back" aria-label="Kortets baksida">
    <div class="brand-mark"></div>
    <div class="brand-name">BrolaTek</div>
    <div class="tagline">ProvKoll | Remarketing | saljportalen-example.se</div>
    <div class="web-links">www.Brolatek-example.com | www.saljportalen-example.se</div>
  </section>

  <section class="card card--front" aria-label="Kortets framsida">
    <div class="brand-name">BrolaTek</div>
    <div class="tagline">ProvKoll | Remarketing | saljportalen-example.se</div>
    <div class="person-name">Per Oskar Fjellström</div>
    <div class="person-role">Founder</div>
    <div class="address">BrolaTek Europe AB<br>Box 8617<br>104 29 Stockholm</div>
    <div class="contacts">
      <span class="label">Direct:</span> +46 70-512 96 47<br>
      <span class="label">Support</span> 08-612 57 394<br>
      <span class="label">Email:</span> po.fjellstrom@brolatek-example.com
    </div>
    <div class="decor-block" role="img" aria-label="Large orange brand graphic area"></div>
  </section>
</body>
</html>
```